New Business Card Design Project

I would like my card design to look exactly like the logo, design, layout, and print of the current attached file. The only change I would like made would be for the print to say THE KMW GROUP instead of THE HALLORAN GROUP. Basically, just replace his group name with my group name. I would also like the backgroud to be the same texture and color as the attached file. I love the dark blue lettering and house logo on the card.

I am completely open to the rest of the card design. I just want something clean and simple. Only basic contact info required on the card. Maybe just name: Kyle M Warrick and cell # 555.914.2087 and email kyle@orchidhomesagent.com

```html
<!DOCTYPE html>
<html lang="en">
<head>
<meta charset="utf-8">
<title>The KMW Group – Business Cards</title>
<link href="https://fonts.googleapis.com/css2?family=Lato:wght@400&family=Oswald:wght@600&display=swap" rel="stylesheet">
<style>
  :root {
    --navy: #2f3384;
    --card: #ffffff;
    --backdrop: #e9e9ec;
  }
  * { margin: 0; padding: 0; box-sizing: border-box; }
  html, body {
    width: 1200px; height: 1200px; overflow: hidden;
    background: var(--backdrop);
  }
  .canvas {
    width: 1200px; height: 1200px;
    display: flex; flex-direction: column;
    align-items: center; justify-content: center;
    gap: 70px;
  }
  .business-card {
    position: relative;
    width: 960px; height: 500px;
    background: var(--card);
    box-shadow: 0 10px 30px rgba(0,0,0,0.12);
    color: var(--navy);
    font-family: "Lato", sans-serif;
    overflow: hidden;
  }
  .brand {
    position: absolute;
    display: flex; flex-direction: column; align-items: flex-start;
  }
  .brand__mark {
    background: var(--navy);
  }
  .brand__name {
    font-weight: 400;
    letter-spacing: -1px;
    white-space: nowrap;
    line-height: 1;
  }
  /* logo side */
  .business-card--back .brand {
    left: 140px; top: 120px;
  }
  .business-card--back .brand__mark {
    width: 130px; height: 130px;
    margin: 0 0 36px 110px;
  }
  .business-card--back .brand__name { font-size: 64px; }
  /* contact side */
  .business-card--front .brand {
    left: 60px; top: 180px;
  }
  .business-card--front .brand__mark {
    width: 100px; height: 100px;
    margin: 0 0 28px 85px;
  }
  .business-card--front .brand__name { font-size: 48px; }
  .contact {
    position: absolute;
    left: 545px; top: 110px;
  }
  .contact__name {
    font-family: "Oswald", sans-serif;
    font-weight: 600;
    font-size: 42px;
    line-height: 1;
    text-transform: uppercase;
    letter-spacing: 0.5px;
  }
  .contact__role {
    font-size: 20px;
    margin-top: 6px;
    margin-left: 30px;
  }
  .contact__list {
    list-style: none;
    margin-top: 24px;
    margin-left: 30px;
  }
  .contact__item {
    display: flex; align-items: center; gap: 14px;
    font-size: 21px;
    margin-bottom: 12px;
    white-space: nowrap;
  }
  .contact__icon { width: 22px; height: 22px; flex: none; }
</style>
</head>
<body>
<main class="canvas">
  <section class="business-card business-card--back">
    <div class="brand">
      <span class="brand__mark"></span>
      <span class="brand__name">THE KMW GROUP</span>
    </div>
  </section>

  <section class="business-card business-card--front">
    <div class="brand">
      <span class="brand__mark"></span>
      <span class="brand__name">THE KMW GROUP</span>
    </div>

    <div class="contact">
      <h1 class="contact__name">Kyle M Warrick</h1>
      <p class="contact__role">Manager</p>
      <ul class="contact__list">
        <li class="contact__item">
          <svg class="contact__icon" viewBox="0 0 24 24" aria-hidden="true">
            <path d="M6.6 10.8a15.1 15.1 0 0 0 6.6 6.6l2.2-2.2a1 1 0 0 1 1-.25 11.4 11.4 0 0 0 3.6.57 1 1 0 0 1 1 1V20a1 1 0 0 1-1 1A17 17 0 0 1 3 4a1 1 0 0 1 1-1h3.5a1 1 0 0 1 1 1c0 1.25.2 2.45.57 3.57a1 1 0 0 1-.25 1z" fill="var(--navy)"/>
          </svg>
          <span>+555-914-2087</span>
        </li>
        <li class="contact__item">
          <svg class="contact__icon" viewBox="0 0 24 24" aria-hidden="true">
            <rect x="2.5" y="5.5" width="19" height="13" fill="none" stroke="var(--navy)" stroke-width="1.5"/>
            <path d="M2.5 5.5 12 13l9.5-7.5M2.5 18.5l7-6M21.5 18.5l-7-6" fill="none" stroke="var(--navy)" stroke-width="1.5"/>
          </svg>
          <span>kyle@orchidhomesagent.com</span>
        </li>
      </ul>
    </div>
  </section>
</main>
</body>
</html>
```